Marrowind Wines - web page for new Australian wine label

We need a landing page for our wine company. Marrowind is a family owned company, we grow the gapes, and make the wine in the Clare valley. Daniel Farrowe is the winemaker and is well known for his style, which is all about the fruit flavour rather than wood or age influences. Marrowind is Abriginal for 2 hills and a water source. We hand pick, hand plunge, foot crush resulting in elegant wine. Little to no additives, minimal filtering, single vineyard wines. Handcrafted with small releases of only the best fruit from carefully selected rows and bunches. The Clare valley is located two hours North of Adelaide, is known for cool climate and slow ripening, resulting in wines that have an elegant mouth feel, with bright colour and outstanding flavours. Our Sevenhill vineyard has a Eastern aspect, gathering morning sun and escaping the hot afternoons, and in our opinion is on of the prettiest valleys in the world. Only 1000 cases per annum of the very best handpicked fruit, from the best rows. We hope you enjoy the Marrowind style, the reds are lighter in colour, fruit driven palate, more old world influence and the Riesling is on the dry side with fresh citrus. Minimal additives and filtering, our aim was to make wine with minimal influence from wine making. Handcrafted wines.

Target Market(s)

females 18 - 60 are the ones that buy 70 percent of wine, so whilst men are also a target, its the ladies we seek to appeal to.

Industry/Entity Type

It Company

Number of Pages Required

4 page

Font styles to use
Serif

Requirements
Must have
• Eye catching front page that makes me feel like i am ordering from quality company, that cares for what they do. Easy to use ordering, and delivery instructions.
• postage is $14.90 per case Australia wide.
• www.marrowindwines-example.com
Nice to have
• I want to see a fun and family oriented business that cares for the wine, we dont make a lot, its buckets and feet. But its wine made wanting to be the best in the world, we dont cut corners on quality. Handcrafted
Should not have
• dont really have any thoughts here, looking for all ideas

```html
<!DOCTYPE html>
<html lang="en">
<head>
<meta charset="utf-8">
<title>Marrowind Wines</title>
<link href="https://fonts.googleapis.com/css2?family=Open+Sans:ital,wght@0,400;0,600;0,700;1,400;1,600&display=swap" rel="stylesheet">
<style>
:root{
  --plum:#4a2350;
  --plum-deep:#2a1530;
  --purple-btn:#5a2f63;
  --blue-logo:#1d5fb0;
  --ink:#222;
  --muted:#555;
  --grey-band:#ececec;
  --gold:#f5a623;
  --white:#fff;
  --foot-text:#e8dfe9;
}
*{box-sizing:border-box;margin:0;padding:0}
html,body{width:1200px;height:3232px;overflow:hidden}
body{font-family:"Open Sans",Arial,sans-serif;color:var(--ink);background:var(--white);position:relative}
section,header,footer{position:relative;width:1200px;overflow:hidden}
.abs{position:absolute}
.center{left:0;right:0;text-align:center}

/* Hero */
.hero{height:659px;background:#26301c}
.hero .photo{position:absolute;inset:0;background:
  radial-gradient(ellipse 420px 300px at 18% 30%,rgba(92,112,66,.85),transparent 70%),
  radial-gradient(ellipse 380px 260px at 75% 22%,rgba(78,98,58,.8),transparent 70%),
  radial-gradient(ellipse 300px 240px at 88% 60%,rgba(52,40,70,.75),transparent 70%),
  radial-gradient(ellipse 360px 260px at 30% 78%,rgba(66,82,46,.8),transparent 70%),
  radial-gradient(ellipse 260px 200px at 60% 85%,rgba(44,34,58,.7),transparent 70%),
  linear-gradient(180deg,#2c3622 0%,#1f2718 100%)}
.hero .shade{position:absolute;inset:0;background:rgba(0,0,0,.22)}
.brand-small{left:76px;top:40px;color:var(--white);font-size:32px;font-weight:400}
.nav{right:72px;top:48px;display:flex;gap:8px;list-style:none}
.nav li{font-size:13px;font-weight:700;color:var(--white);padding:7px 15px;letter-spacing:.3px}
.nav li.active{background:var(--purple-btn);border:2px solid var(--white);border-radius:18px;padding:5px 16px}
.hero-brand{top:232px;color:var(--white);font-size:88px;font-weight:400;line-height:1}
.hero-sub{top:336px;color:var(--white);font-size:26px;font-style:italic}
.hero-tag{top:392px;color:var(--white);font-size:31px;font-weight:700;line-height:42px}
.dots{top:600px;display:flex;justify-content:center;gap:7px}
.dots span{width:14px;height:14px;border-radius:50%;background:var(--white)}
.dots span.off{background:transparent;border:2px solid var(--white)}

/* Buttons */
.btn{display:inline-block;border:2px solid var(--plum);border-radius:22px;color:var(--plum);font-size:12px;font-weight:700;letter-spacing:.4px;text-align:center;line-height:38px;height:42px}

/* Welcome */
.welcome{height:403px}
.welcome h2{top:42px;font-size:28px;font-weight:400;letter-spacing:.5px}
.welcome .brand-blue{top:86px;font-size:50px;color:var(--blue-logo)}
.welcome p{top:178px;left:108px;right:108px;text-align:center;font-size:17px;font-style:italic;line-height:32px;color:var(--muted)}
.welcome .btn{top:310px;left:525px;width:150px}

/* Our wine */
.wine{height:390px;background:var(--grey-band)}
.wine .photo{right:0;top:0;width:640px;height:390px;background:
  radial-gradient(ellipse 70px 190px at 480px 240px,#1c2036,transparent 72%),
  radial-gradient(ellipse 140px 70px at 170px 330px,rgba(190,50,30,.85),transparent 72%),
  linear-gradient(180deg,#7d97ad 0%,#a9bccb 32%,#c4c9bf 48%,#e4e4dc 62%,#dcdfe2 100%)}
.wine .fade{right:0;top:0;width:640px;height:390px;background:linear-gradient(90deg,var(--grey-band) 0%,rgba(236,236,236,.85) 14%,rgba(236,236,236,0) 34%)}
.wine h2{left:75px;top:62px;font-size:27px;font-weight:400}
.wine p{left:75px;top:118px;width:600px;font-size:15px;line-height:33px;color:var(--muted)}
.wine .btn{left:75px;top:282px;width:152px}

/* Process */
.process{height:622px}
.process h2{top:46px;font-size:27px;font-weight:400}
.process .lead{top:100px;left:100px;right:100px;text-align:center;font-size:15px;line-height:28px;color:var(--muted)}
.card{top:196px;width:330px;height:377px}
.card .photo{position:absolute;inset:0;background:
  radial-gradient(ellipse 120px 150px at 40% 35%,rgba(30,36,70,.9),transparent 72%),
  linear-gradient(135deg,#8a6a3a 0%,#c08060 40%,#6a3a50 70%,#4a2257 100%)}
.card .photo.b{background:
  radial-gradient(ellipse 90px 120px at 50% 40%,rgba(180,80,50,.8),transparent 72%),
  linear-gradient(180deg,#8a8f90 0%,#4e5a3a 35%,#5c4552 65%,#4a2257 100%)}
.card .photo.c{background:
  radial-gradient(ellipse 130px 110px at 55% 40%,rgba(200,160,130,.55),transparent 72%),
  linear-gradient(180deg,#4a3f48 0%,#3e3448 45%,#4a2257 100%)}
.card .tint{position:absolute;left:0;right:0;bottom:0;height:190px;background:linear-gradient(180deg,rgba(74,34,87,0),rgba(74,34,87,.9))}
.card h3{position:absolute;left:0;right:0;top:282px;text-align:center;color:var(--white);font-size:19px;font-weight:700;letter-spacing:.5px}
.card p{position:absolute;left:20px;right:20px;top:314px;text-align:center;color:var(--white);font-size:15px;font-weight:600;line-height:28px}

/* Delivery */
.delivery{height:265px;background:#3a4450}
.delivery .photo{position:absolute;inset:0;background:
  linear-gradient(180deg,#5a6370 0%,#4c5662 40%,#38424e 62%,#2a3644 78%,#22303e 100%)}
.delivery .shade{position:absolute;inset:0;background:rgba(20,24,32,.25)}
.delivery h2{top:88px;color:var(--white);font-size:33px;font-weight:700;line-height:42px;letter-spacing:.5px}
.delivery h2 em{font-style:normal;color:var(--gold)}

/* Gallery */
.gallery{height:532px}
.gallery h2{top:46px;font-size:27px;font-weight:400}
.tile{width:255px;height:177px}
.g1{background:radial-gradient(ellipse at 45% 40%,#3a3450,transparent 60%),linear-gradient(135deg,#56683a,#2c3224)}
.g2{background:radial-gradient(ellipse at 55% 75%,#c0a040,transparent 45%),linear-gradient(135deg,#9a9a96,#4a4a48)}
.g3{background:radial-gradient(ellipse at 50% 70%,#a8a8a4,transparent 50%),linear-gradient(180deg,#4a7a3a,#6a5a48)}
.g4{background:radial-gradient(ellipse at 40% 70%,#c8b040,transparent 40%),linear-gradient(180deg,#8fb0d6 0%,#b8c8d8 35%,#6f8a4a 65%,#5a5a3a 100%)}
.g5{background:radial-gradient(ellipse at 45% 55%,#a04a30,transparent 40%),linear-gradient(135deg,#7a6a3a,#3a3a28)}
.g6{background:radial-gradient(ellipse at 50% 40%,#b08a78,transparent 45%),linear-gradient(135deg,#5a2f4a,#2a2030)}
.g7{background:radial-gradient(ellipse at 40% 45%,#c09050,transparent 50%),linear-gradient(135deg,#6a5a30,#2a2220)}
.g8{background:radial-gradient(ellipse at 65% 65%,#d07040,transparent 35%),linear-gradient(180deg,#a8b8c8,#8a8a88 55%,#6a5a48)}

/* Footer */
.footer{height:361px;background:linear-gradient(135deg,#3a1c40 0%,var(--plum-deep) 50%,#3e1f45 100%);color:var(--foot-text)}
.footer .brand-small{left:76px;top:40px}
.footer .about{left:76px;top:118px;width:220px;font-size:13px;line-height:22px}
.footer h4{font-size:16px;font-weight:400;color:var(--white)}
.col-map{left:362px;top:40px}
.col-map ul{list-style:none;margin-top:10px}
.col-map li{font-size:13px;line-height:25px}
.col-contact{left:565px;top:40px;font-size:13px}
.col-contact .name{margin-top:10px;font-weight:700;font-size:15px;color:var(--white)}
.col-contact .addr{margin-top:12px;line-height:22px}
.col-contact .row{display:flex;align-items:center;gap:10px;margin-top:14px}
.col-news{left:817px;top:40px}
.col-news .field{margin-top:14px;width:256px;height:34px;border-radius:17px;background:var(--white);color:#333;font-size:12px;padding-left:18px;line-height:34px}
.col-news .signup{margin-top:10px;margin-left:164px;width:86px;height:32px;border-radius:16px;background:#1a0e1c;color:var(--white);font-size:12px;font-weight:700;text-align:center;line-height:32px}
.col-news h4.connect{margin-top:30px}
.social{display:flex;gap:17px;margin-top:14px}
.social span{width:17px;height:17px;border-radius:3px;background:var(--white)}
.rule{left:76px;right:76px;top:285px;height:1px;background:rgba(255,255,255,.2)}
.copy{top:313px;font-size:12px}
</style>
</head>
<body>

<header class="hero">
  <div class="photo" role="img" aria-label="Photograph of vine leaves and ripe grape bunches"></div>
  <div class="shade"></div>
  <div class="abs brand-small">Marrowind</div>
  <ul class="abs nav">
    <li class="active">HOME</li><li>ABOUT US</li><li>OUR WINE</li><li>HOW IT WORKS</li><li>BLOG</li><li>GALLERY</li><li>CONTACT US</li>
  </ul>
  <div class="abs center hero-brand">Marrowind</div>
  <div class="abs center hero-sub">2016 Riesling Clare Valley</div>
  <div class="abs center hero-tag">Only 1000 cases per annum of the very best handpicked<br>fruit, from the best rows.</div>
  <div class="abs center dots"><span class="off"></span><span></span><span></span><span></span></div>
</header>

<section class="welcome">
  <h2 class="abs center">WELCOME TO</h2>
  <div class="abs center brand-blue">Marrowind</div>
  <p class="abs">Aliquam molestie, mi et imperdiet euismod, dui purus auctor tellus, et interdum lacus lectus et ante. Sed accumsan<br>sollicitudin sapien, sit amet adipiscing turpis gravida ac. In congue, neque ac lobortis volutpat, libero mauris<br>varius&nbsp; mi, vitae suscipit ipsum ligula vitae risus.</p>
  <span class="abs btn">READ MORE</span>
</section>

<section class="wine">
  <div class="abs photo" role="img" aria-label="Photograph of a wine bottle beside a bowl of lobster on a beach"></div>
  <div class="abs fade"></div>
  <h2 class="abs">OUR WINE</h2>
  <p class="abs">Aliquam molestie, mi et imperdiet euismod, dui purus auctor tellus, et interdum<br>lacus lectus et ante. Sed accumsan sollicitudin sapien, sit amet adipiscing turpis<br>gravida ac. In congue, neque ac lobortis volutpat, libero mauris<br>varius&nbsp; mi, vitae suscipit ipsum ligula vitae risus.</p>
  <span class="abs btn">READ MORE</span>
</section>

<section class="process">
  <h2 class="abs center">OUR WORKING PROCESS</h2>
  <p class="abs lead">Aliquam molestie, mi et imperdiet euismod, dui purus auctor tellus, et interdum lacus lectus et ante. Sed accumsan sollicitudin sapien,<br>sit amet adipiscing turpis gravida ac.</p>
  <div class="abs card" style="left:75px">
    <div class="photo" role="img" aria-label="Photograph of a hand holding a grape bunch"></div><div class="tint"></div>
    <h3>HAND PICK</h3><p>Sed accumsan sollicitudin sit amet turpis gravida ac.</p>
  </div>
  <div class="abs card" style="left:434px">
    <div class="photo b" role="img" aria-label="Photograph of a picker holding grapes among the vines"></div><div class="tint"></div>
    <h3>HAND PLUNGE</h3><p>Sed accumsan sollicitudin sit amet turpis gravida ac.</p>
  </div>
  <div class="abs card" style="left:793px">
    <div class="photo c" role="img" aria-label="Photograph of hands plunging crushed grapes"></div><div class="tint"></div>
    <h3>FOOT CRUSH</h3><p>Sed accumsan sollicitudin sit amet turpis gravida ac.</p>
  </div>
</section>

<section class="delivery">
  <div class="photo" role="img" aria-label="Photograph of a harbour city skyline"></div>
  <div class="shade"></div>
  <h2 class="abs center">DELIVERY CHARGE IS <em>$14.90 PER CASE</em><br>AUSTRALIA WIDE.</h2>
</section>

<section class="gallery">
  <h2 class="abs center">PHOTO GALLERY</h2>
  <div class="abs tile g1" style="left:75px;top:106px" role="img" aria-label="Photograph of grape bunches on the vine"></div>
  <div class="abs tile g2" style="left:340px;top:106px" role="img" aria-label="Photograph of winery equipment and a forklift"></div>
  <div class="abs tile g3" style="left:605px;top:106px" role="img" aria-label="Photograph of workers at a steel fermentation tank"></div>
  <div class="abs tile g4" style="left:870px;top:106px" role="img" aria-label="Photograph of the harvest crew in the vineyard"></div>
  <div class="abs tile g5" style="left:75px;top:293px" role="img" aria-label="Photograph of a picker among the vines"></div>
  <div class="abs tile g6" style="left:340px;top:293px" role="img" aria-label="Photograph of hands in crushed grapes"></div>
  <div class="abs tile g7" style="left:605px;top:293px" role="img" aria-label="Photograph of family gathered in the cellar"></div>
  <div class="abs tile g8" style="left:870px;top:293px" role="img" aria-label="Photograph of grapes being tipped into a bin"></div>
</section>

<footer class="footer">
  <div class="abs brand-small">Marrowind</div>
  <p class="abs about">Lorem ipsum dolor sit amet, consect- etuer adipiscing elit, sed diam nonummy nibh euismod tincidunt ut laoreet dolore</p>
  <div class="abs col-map">
    <h4>Site Map</h4>
    <ul><li>Home</li><li>About Us</li><li>Our Wine</li><li>How it Works</li><li>Blog</li><li>Gallery</li><li>Contact Us</li></ul>
  </div>
  <div class="abs col-contact">
    <h4>Contact Info</h4>
    <div class="name">Marrowind</div>
    <div class="addr">42 Wattle Lane<br>Sevenhill, SA 5453</div>
    <div class="row"><svg width="14" height="14" viewBox="0 0 24 24"><path fill="#fff" d="M6.6 10.8a15 15 0 0 0 6.6 6.6l2.2-2.2c.3-.3.7-.4 1-.2 1.1.4 2.3.6 3.6.6.6 0 1 .4 1 1V20c0 .6-.4 1-1 1A17 17 0 0 1 3 4c0-.6.4-1 1-1h3.5c.6 0 1 .4 1 1 0 1.3.2 2.5.6 3.6.1.3 0 .7-.2 1z"/></svg>1-800-555-0142</div>
    <div class="row"><svg width="14" height="12" viewBox="0 0 24 20"><path fill="#fff" d="M2 2h20v16H2z"/><path fill="none" stroke="#3a1c40" stroke-width="2" d="M2 3l10 8 10-8"/></svg>hello@marrowindwines-example.com</div>
    <div class="row"><svg width="12" height="16" viewBox="0 0 16 22"><path fill="#fff" d="M8 0a8 8 0 0 1 8 8c0 6-8 14-8 14S0 14 0 8a8 8 0 0 1 8-8z"/><circle cx="8" cy="8" r="3" fill="#3a1c40"/></svg>Map Location</div>
  </div>
  <div class="abs col-news">
    <h4>Sign Up Newsletter</h4>
    <div class="field">Enter Email Address</div>
    <div class="signup">Sign Up</div>
    <h4 class="connect">Connect Us</h4>
    <div class="social" aria-label="Social links"><span></span><span></span><span></span><span></span><span></span><span></span><span></span></div>
  </div>
  <div class="abs rule"></div>
  <div class="abs center copy">Copyright© 2017. Company Name. All Right Reserved</div>
</footer>

</body>
</html>
```